Lantern Hearthworks Business Cards

Looking to create simple business cards that highlight our unique three sided triangle fire pit design with the colors and font of our logo, listed below.

Requirements
Must have
• Looking for something simple that includes a picture of our fire pit with name, website (lanternhearthworks.com), phone number and email. Want to keep the color mostly orange and black.
• Font is gotham(medium) and orange color code is #ee6e22

```html
<!DOCTYPE html>
<html lang="en">
<head>
<meta charset="utf-8">
<title>Lantern Hearthworks Business Cards</title>
<link rel="stylesheet" href="https://fonts.googleapis.com/css2?family=Montserrat:wght@400;500;600&display=swap">
<style>
  :root {
    --orange: #ee6e22;
    --ink: #0d0d0d;
    --card-black: #111111;
    --white: #f2f2f2;
    --rule: #4a4a4a;
    --backdrop: #e4e4e4;
    --stone: #3a3a3a;
  }
  * { margin: 0; padding: 0; box-sizing: border-box; }
  html, body { width: 1200px; height: 1021px; overflow: hidden; }
  body {
    background: var(--backdrop);
    font-family: "Montserrat", Arial, sans-serif;
    font-weight: 500;
    position: relative;
  }
  .card {
    position: absolute;
    left: 220px;
    width: 760px;
    height: 434px;
    box-shadow: 0 14px 30px rgba(0,0,0,0.25);
  }
  .card--photo {
    top: 50px;
    background: var(--orange);
    padding: 16px;
  }
  .card__photo {
    width: 100%;
    height: 100%;
    background:
      radial-gradient(ellipse 22% 34% at 52% 48%, #f38a2c 0%, #c9521b 35%, rgba(40,30,25,0) 100%),
      radial-gradient(ellipse at 50% 50%, #4a4a4a 0%, var(--stone) 45%, #262626 100%);
  }
  .card--contact {
    top: 537px;
    background: var(--card-black);
    color: var(--white);
    overflow: hidden;
  }
  .brand {
    position: absolute;
    left: 70px;
    top: 78px;
    display: flex;
    align-items: center;
    gap: 22px;
  }
  .brand__mark {
    width: 34px;
    height: 34px;
    background: var(--orange);
  }
  .brand__rule {
    width: 1px;
    height: 96px;
    background: var(--rule);
  }
  .brand__name {
    font-size: 28px;
    letter-spacing: 6px;
    line-height: 1.15;
    color: var(--white);
    text-transform: uppercase;
  }
  .contact {
    position: absolute;
    left: 70px;
    bottom: 80px;
    list-style: none;
    font-size: 21px;
    font-weight: 400;
    line-height: 1.35;
  }
  .contact li { display: flex; align-items: center; gap: 12px; }
  .contact svg { width: 18px; height: 18px; flex: none; }
  .person {
    position: absolute;
    right: 92px;
    top: 232px;
    text-align: right;
  }
  .person__name {
    color: var(--orange);
    font-size: 26px;
    font-weight: 600;
    letter-spacing: 1px;
  }
  .person__role {
    font-size: 20px;
    font-weight: 400;
    letter-spacing: 1px;
    margin-top: 2px;
  }
  .edge-tab {
    position: absolute;
    right: 0;
    top: 262px;
    width: 26px;
    height: 48px;
    background: var(--orange);
  }
  .base-band {
    position: absolute;
    left: 0;
    right: 0;
    bottom: 0;
    height: 64px;
    background: #161616;
  }
</style>
</head>
<body>
  <section class="card card--photo">
    <div class="card__photo" role="img" aria-label="Photo of a triangular steel fire pit with burning logs on dark gravel"></div>
  </section>

  <section class="card card--contact">
    <div class="base-band"></div>
    <div class="brand">
      <span class="brand__mark"></span>
      <span class="brand__rule"></span>
      <p class="brand__name">Lantern<br>Hearthworks</p>
    </div>

    <ul class="contact">
      <li>
        <svg viewBox="0 0 24 24" aria-hidden="true"><path fill="#ee6e22" d="M6.6 10.8a15.1 15.1 0 0 0 6.6 6.6l2.2-2.2a1 1 0 0 1 1-.25 11.4 11.4 0 0 0 3.6.57 1 1 0 0 1 1 1V20a1 1 0 0 1-1 1A17 17 0 0 1 3 4a1 1 0 0 1 1-1h3.5a1 1 0 0 1 1 1c0 1.25.2 2.45.57 3.57a1 1 0 0 1-.25 1z"/></svg>
        503-555-0187
      </li>
      <li>
        <svg viewBox="0 0 24 24" aria-hidden="true"><rect x="3" y="5" width="18" height="14" fill="none" stroke="#ee6e22" stroke-width="2"/><path d="M3 6l9 7 9-7" fill="none" stroke="#ee6e22" stroke-width="2"/></svg>
        hello@lanternhearthworks.com
      </li>
      <li>
        <svg viewBox="0 0 24 24" aria-hidden="true"><circle cx="12" cy="12" r="9" fill="none" stroke="#ee6e22" stroke-width="2"/><path d="M3 12h18M12 3c3 3 3 15 0 18M12 3c-3 3-3 15 0 18" fill="none" stroke="#ee6e22" stroke-width="1.6"/></svg>
        lanternhearthworks.com
      </li>
    </ul>

    <div class="person">
      <p class="person__name">Dale Marwick</p>
      <p class="person__role">Co-Founder</p>
    </div>
    <span class="edge-tab"></span>
  </section>
</body>
</html>
```